Flyer for customer acquisition.

Hello, We are a sportmanagement agency from Germany and we need information flyers for customer acquisition. It should be DinA4 and should have a modern but serious design. I have uploaded a information sheet, where you can find the text and the composition, the flyer should have. I also uploaded Pictures / Images, which you can use. Of course you can use other suitable images. If they are not free, I will buy them later. On the bottom of the flyer there has been the contact information. You will find them in the download section, too. If you have questions, just write me. If I forgot something, I will update the letter :) Thank you very much!
Ich brauche zusätzliche Tage um durchzusehen

```html
<!DOCTYPE html>
<html lang="de">
<head>
<meta charset="utf-8">
<title>NOVA-S Nachwuchsförderung</title>
<link href="https://fonts.googleapis.com/css2?family=Oswald:wght@500&family=Raleway:wght@400;600;700&display=swap" rel="stylesheet">
<style>
  :root{
    --blue:#12a3d4;
    --blue-deep:#0f86b8;
    --black:#0b0b0b;
    --ink:#1a1a1a;
    --grey:#e6e7e9;
    --line:#6b3b2a;
    --white:#ffffff;
  }
  *{margin:0;padding:0;box-sizing:border-box}
  html,body{width:974px;height:1200px;overflow:hidden;background:var(--white)}
  .flyer{position:relative;width:974px;height:1200px;font-family:"Raleway",sans-serif;color:var(--ink)}
  .shapes{position:absolute;inset:0;width:974px;height:1200px}
  .team-photo{position:absolute;left:77px;top:7px;width:310px;height:131px;
    background:linear-gradient(180deg,#cfcfcf 0%,#3a3a3a 55%,#111 100%)}
  .title{position:absolute;left:61px;top:160px;font-family:"Oswald",sans-serif;font-weight:500;
    font-size:33px;color:var(--white);letter-spacing:.2px}
  .brand{position:absolute;left:650px;top:137px;width:220px;text-align:center;
    font-weight:700;font-size:38px;color:var(--white);letter-spacing:1px}
  .tagline{position:absolute;left:61px;top:250px;font-weight:700;font-size:21px;line-height:22px;color:var(--blue)}
  .hero-image{position:absolute;left:0;top:318px;width:361px;height:751px;
    background:linear-gradient(180deg,#d8d8d8 0%,#9c9696 35%,#b9d9ea 70%,#e8f5fb 100%)}
  .service{position:absolute;width:240px}
  .icon{width:80px;height:80px;border-radius:50%;background:var(--blue);color:var(--white);
    display:flex;align-items:center;justify-content:center;text-align:center;
    font-weight:600;font-size:10px;line-height:12px;letter-spacing:.3px;margin-left:0;margin-bottom:13px}
  .service h2{font-size:16.5px;font-weight:700;line-height:20px;color:var(--ink)}
  .service p{font-size:13.4px;line-height:16.6px;margin-top:2px;color:var(--ink)}
  .notes{position:absolute;left:0;top:1075px;width:974px;text-align:center;color:var(--white);
    font-size:9.6px;line-height:12.5px}
  .notes .second{margin-top:3px}
  .contact{position:absolute;left:0;top:1147px;width:974px;height:39px;line-height:39px;text-align:center;
    color:var(--white);font-size:18px;letter-spacing:1.8px}
</style>
</head>
<body>
<main class="flyer">
  <svg class="shapes" viewBox="0 0 994 1285" preserveAspectRatio="none" aria-hidden="true">
    <defs>
      <linearGradient id="swoosh" x1="0" y1="0" x2="1" y2="0">
        <stop offset="0" stop-color="#e4e5e7"/><stop offset="1" stop-color="#f4f4f5"/>
      </linearGradient>
      <linearGradient id="banner" x1="0" y1="0" x2="1" y2="1">
        <stop offset="0" stop-color="#17a9d8"/><stop offset="1" stop-color="#1583b2"/>
      </linearGradient>
    </defs>
    <path d="M0,245 H540 C480,262 450,345 385,352 L0,355 Z" fill="url(#swoosh)"/>
    <path d="M0,356 H365 C425,352 445,276 520,272 H760" fill="none" stroke="var(--line)" stroke-width="1.4"/>
    <path d="M0,146 H455 C495,146 520,205 572,245 H0 Z" fill="var(--black)"/>
    <path d="M465,135 C520,128 540,42 605,42 H994 V285 H690 C615,285 565,150 465,135 Z" fill="url(#banner)"/>
    <path d="M0,1000 C0,1100 40,1140 150,1145 H0 Z" fill="var(--black)"/>
    <rect x="0" y="1145" width="994" height="83" fill="var(--black)"/>
    <rect x="0" y="1228" width="994" height="42" fill="var(--blue)"/>
    <rect x="0" y="1270" width="994" height="15" fill="var(--black)"/>
  </svg>

  <div class="team-photo" role="img" aria-label="Foto der drei Geschäftsführer im Anzug"></div>
  <h1 class="title">NOVA-S NACHWUCHSFÖRDERUNG</h1>
  <div class="brand">NOVA-S</div>
  <p class="tagline">Wir begleiten dich auf<br>deinem Weg zum Profi</p>
  <div class="hero-image" role="img" aria-label="Illustration eines Fußballspielers mit Ball in Grau- und Blautönen"></div>

  <section class="service" style="left:406px;top:353px">
    <div class="icon">ICON<br>WILL<br>COME<br>HERE</div>
    <h2>Karriereplanung</h2>
    <p>Wir haben deine Karriere im Blick! In enger Absprache mit deinen Eltern und dir leiten wir die richtigen Maßnahmen und Schritte ein, um dein Ziel „Profifußballer“ zu realisieren.</p>
  </section>
  <section class="service" style="left:663px;top:353px">
    <div class="icon">ICON<br>WILL<br>COME<br>HERE</div>
    <h2>Ständiger Ansprechpartner</h2>
    <p>Egal um welchen Themen es sich handelt, wir sind für dich da! Ein vertrauensvolles und freundschaftliches Verhältnis ist uns besonders wichtig.</p>
  </section>
  <section class="service" style="left:406px;top:569px">
    <div class="icon">ICON<br>WILL<br>COME<br>HERE</div>
    <h2>Rechtsberatung<br>/Vertragsrecht</h2>
    <p>Juristendeutsch und Kleingedrucktes? Kein Problem! Wir helfen dir den Durchblick zu behalten und holen immer das Beste für dich raus.</p>
  </section>
  <section class="service" style="left:663px;top:569px">
    <div class="icon">ICON<br>WILL<br>COME<br>HERE</div>
    <h2>Ausrüstung</h2>
    <p>Wir besorgen dir deine Ausrüstung! Unsere Beziehungen zu den großen Sportartikelherstellern ermöglichen den Abschluss von Ausrüsterverträgen*.</p>
  </section>
  <section class="service" style="left:406px;top:793px">
    <div class="icon">ICON<br>WILL<br>COME<br>HERE</div>
    <h2>Kooperationspartner/<br>Netzwerk</h2>
    <p>Ob Entscheidungsträger oder Experte, wir kennen die richtigen Leute. Zusätzlich bieten wir dir eine große Bandbreite an Leistungen, die du jederzeit in Anspruch nehmen kannst**.</p>
  </section>
  <section class="service" style="left:663px;top:793px">
    <div class="icon">ICON<br>WILL<br>COME<br>HERE</div>
    <h2>Vorsorge</h2>
    <p>Verletzungen gehören leider zum Fußball dazu. Wir sichern dich ab, indem wir eine private Zusatzkrankenversicherung für dich abschließen.</p>
  </section>

  <div class="notes">
    <p>*Die Entscheidung über das Zustandekommen eines Ausrüstervertrags obliegt dem jeweiligen Sportartikelhersteller. Ist ein Abschluss aktuell nicht<br>möglich, erhältst du von uns 2x pro Saison neue Fußballschuhe sowie weitere Ausrüstungsgegenstände.</p>
    <p class="second">**Personal Training, Athletik-Training, Ernährungsberatung, Sportpsychologische Betreuung, uvm</p>
  </div>
  <p class="contact">Tel.: 01234/5678900 | E-Mail: info@nova-s.de | web: www.nova-s.de</p>
</main>
</body>
</html>
```